Task Scheduling Web App

I have a basic web app that I need designed. It must be mobile-first but it needs to be responsive for desktop users as well.
1. Before beginning the exercise, the user inputs basic info on their country and age.
2. The user is then presented with two piles of cards (TASK or DAY), with the top card face up. They have 20 seconds before their combination is set, during which they can replace either of the cards at random as many times as they like. At any time they find a combination they’re happy with, they can progress to the next screen. If the clock runs out the combination is set based on whatever cards are showing at the time and they’re moved on to the next screen.
3. The user is presented with a blank graph; x axis is ‘How important is it?’, y axis is ‘How often does it need to be done?’. The two cards they picked in the previous screen are combined to create a COMBO and the user must place a mark somewhere on the graph to represent how important they believe the scheduled task to be vs how often it will need to be done.
4. Once the user has picked a spot on the graph, options appear for them to re-do the exercise by choosing a new combo or to progress and see how their peers are organising their tasks.
5. If they choose to view insights, they must login with Villowry so a popup will appear to facilitate this.
6. After logging in with Villowry, users can view the top 10 combinations for their demographic listed and mapped on a graph. This information is based on the selection and ranking of combinations by other users.

```html
<!DOCTYPE html>
<html lang="en">
<head>
<meta charset="utf-8">
<title>Task Scheduling App – Screens</title>
<link rel="stylesheet" href="https://fonts.googleapis.com/css2?family=Noto+Serif:wght@400&family=Archivo:wght@400;800&family=Arimo:wght@400&display=swap">
<style>
  :root {
    --bg: #b4bcc2;
    --orange-top: #fb9b35;
    --orange-bottom: #ee9a26;
    --navy: #2f2e63;
    --white: #ffffff;
    --paper: #f6f6f6;
    --control: #ececec;
    --ink: #111111;
  }
  * { box-sizing: border-box; margin: 0; padding: 0; }
  html, body { width: 1200px; height: 1000px; overflow: hidden; }
  body { background: var(--bg); position: relative; font-family: "Arimo", sans-serif; }

  .screen {
    position: absolute;
    width: 426px;
    height: 688px;
    overflow: hidden;
    background: linear-gradient(180deg, var(--orange-top), var(--orange-bottom));
  }
  .screen--prioritize { left: 174px; top: 208px; z-index: 1; }
  .screen--pick { left: 384px; top: 149px; z-index: 2; }
  .screen--user { left: 592px; top: 90px; z-index: 3; }

  .screen-title {
    position: absolute;
    font-family: "Noto Serif", serif;
    font-weight: 400;
    color: var(--white);
    white-space: nowrap;
    line-height: 1;
  }

  /* Prioritize screen */
  .screen--prioritize .screen-title { left: 40px; top: 56px; font-size: 44px; }
  .chart { position: absolute; left: 0; top: 130px; width: 426px; height: 260px; }
  .chart-label {
    position: absolute;
    font-family: "Noto Serif", serif;
    font-size: 12px;
    color: var(--white);
  }
  .axis-caption {
    position: absolute;
    font-size: 11px;
    color: var(--white);
    white-space: nowrap;
  }
  .axis-caption--y {
    left: 52px; top: 112px;
    transform: rotate(-90deg);
    transform-origin: left top;
  }
  .task-card { position: absolute; left: 40px; top: 432px; width: 330px; height: 186px; }
  .task-card__face {
    height: 132px;
    background: var(--white);
    display: flex; align-items: center;
    padding-left: 52px;
    font-size: 30px;
    color: var(--navy);
  }
  .task-card__bar {
    height: 54px;
    background: var(--navy);
    color: var(--white);
    font-size: 30px;
    padding: 10px 0 0 110px;
  }

  /* Pick screen */
  .pick-title { left: 70px; top: 64px; font-size: 44px; }
  .pick-combo {
    position: absolute; left: 150px; top: 104px;
    font-family: "Noto Serif", serif; font-size: 38px;
    color: var(--navy); letter-spacing: 1px;
  }
  .card-pile { position: absolute; left: 72px; width: 260px; height: 154px; }
  .card-pile--task { top: 175px; }
  .card-pile--day { top: 377px; }
  .card-pile span {
    position: absolute; width: 240px; height: 146px;
    background: var(--paper);
    border: 1px solid #e2e2e2;
  }
  .card-pile span:nth-child(1) { left: 0; top: 0; }
  .card-pile span:nth-child(2) { left: 5px; top: 4px; }
  .card-pile span:nth-child(3) { left: 11px; top: 8px; background: var(--white); }
  .pile-divider {
    position: absolute; left: 48px; top: 355px;
    width: 330px; height: 3px; background: var(--navy);
  }
  .pick-button {
    position: absolute; left: 66px; top: 571px;
    width: 300px; height: 54px;
    border: 3px solid var(--navy);
  }
  .pick-button::after {
    content: ""; position: absolute; left: 126px; top: 24px;
    width: 44px; height: 4px; background: var(--navy);
  }

  /* User info screen */
  .user-title {
    left: 0; right: 0; top: 124px; text-align: center;
    font-size: 50px;
  }
  .select {
    position: absolute; left: 89px;
    width: 265px; height: 50px;
    background: var(--control);
    border-radius: 10px;
    display: flex;
    font-family: "Archivo", sans-serif;
    font-weight: 800;
    font-size: 20px;
    letter-spacing: 1.5px;
    color: var(--ink);
  }
  .select--country { top: 252px; }
  .select--age { top: 328px; }
  .select__label {
    flex: 1; display: flex; align-items: center; justify-content: center;
    border-right: 2px solid #c9c9c9;
  }
  .select__arrow { width: 63px; display: flex; align-items: center; justify-content: center; }
  .go-button {
    position: absolute; left: 66px; top: 479px;
    width: 302px; height: 52px;
    border: 3px solid var(--navy);
    display: flex; align-items: center; justify-content: center;
    font-family: "Archivo", sans-serif;
    font-size: 26px;
    color: var(--white);
    letter-spacing: 1px;
  }
</style>
</head>
<body>

  <section class="screen screen--prioritize">
    <h2 class="screen-title">Prioritize</h2>
    <div class="chart">
      <svg width="426" height="260" viewBox="0 0 426 260" aria-hidden="true">
        <line x1="71" y1="9" x2="71" y2="225" stroke="#2f2e63" stroke-width="2"/>
        <line x1="71" y1="225" x2="420" y2="225" stroke="#2f2e63" stroke-width="2"/>
        <line x1="61" y1="9" x2="71" y2="9" stroke="#2f2e63" stroke-width="1.5"/>
        <line x1="61" y1="225" x2="71" y2="225" stroke="#2f2e63" stroke-width="1.5"/>
        <line x1="71" y1="225" x2="71" y2="233" stroke="#2f2e63" stroke-width="1.5"/>
      </svg>
      <span class="chart-label" style="left:20px;top:0">Huge</span>
      <span class="chart-label" style="left:20px;top:216px">None</span>
      <span class="chart-label" style="left:64px;top:233px;font-size:10px">1x</span>
      <span class="axis-caption axis-caption--y">How important is it?</span>
      <span class="axis-caption" style="left:117px;top:230px">How often does it need to be done?</span>
    </div>
    <div class="task-card">
      <div class="task-card__face">Task</div>
      <div class="task-card__bar">Combo</div>
    </div>
  </section>

  <section class="screen screen--pick">
    <h2 class="screen-title pick-title">Pick a</h2>
    <div class="pick-combo">COMBO</div>
    <div class="card-pile card-pile--task"><span></span><span></span><span></span></div>
    <div class="pile-divider"></div>
    <div class="card-pile card-pile--day"><span></span><span></span><span></span></div>
    <div class="pick-button"></div>
  </section>

  <section class="screen screen--user">
    <h1 class="screen-title user-title">User Info</h1>
    <div class="select select--country">
      <span class="select__label">COUNTRY</span>
      <span class="select__arrow"><svg width="24" height="16" viewBox="0 0 24 16" aria-hidden="true"><path d="M0 0h24L12 16z" fill="#111"/></svg></span>
    </div>
    <div class="select select--age">
      <span class="select__label">AGE RANGE</span>
      <span class="select__arrow"><svg width="24" height="16" viewBox="0 0 24 16" aria-hidden="true"><path d="M0 0h24L12 16z" fill="#111"/></svg></span>
    </div>
    <div class="go-button">GO!</div>
  </section>

</body>
</html>
```